MSA Plans

I would like to rebuild my brochure for the 3 business plans that I currently offer my clients. I would like to make it look much more modern & attractive to clients when choosing one of our service plans. If we can stick to a tech theme that would be great. Message me for anymore information.

```html
<!DOCTYPE html>
<html lang="en">
<head>
<meta charset="utf-8">
<title>Managed Services Framework</title>
<link rel="stylesheet" href="https://fonts.googleapis.com/css2?family=Outfit:wght@300;400;500;600;800&display=swap">
<style>
  :root {
    --navy-deep: #0a1236;
    --navy: #13246e;
    --row: #151c30;
    --line: #5c2a24;
    --orange: #ff3f06;
    --white: #ffffff;
    --tick: #3ddc1c;
    --cross: #f01818;
  }
  * { margin: 0; padding: 0; box-sizing: border-box; }
  html, body { width: 927px; height: 1200px; overflow: hidden; }
  body {
    position: relative;
    font-family: "Outfit", sans-serif;
    color: var(--white);
    background: var(--navy-deep);
  }
  .network-backdrop {
    position: absolute; inset: 0;
    background:
      radial-gradient(circle at 15% 10%, rgba(40,90,255,.35), transparent 40%),
      radial-gradient(circle at 90% 20%, rgba(40,90,255,.3), transparent 40%),
      radial-gradient(circle at 50% 75%, rgba(30,60,200,.35), transparent 55%),
      linear-gradient(180deg, #0d1a52 0%, #0b1543 60%, #0a1238 100%);
  }
  .brand {
    position: absolute; top: 50px; left: 0; width: 100%;
    display: flex; justify-content: center; align-items: center; gap: 14px;
  }
  .brand-dot { width: 46px; height: 46px; border-radius: 50%; background: var(--white); }
  .brand-text { display: flex; flex-direction: column; }
  .brand-name { font-weight: 600; font-size: 44px; letter-spacing: 6px; line-height: 1; }
  .brand-tagline { font-weight: 600; font-size: 9.5px; letter-spacing: 3.2px; margin-top: 4px; }
  .title-pill {
    position: absolute; top: 153px; left: 254px; width: 419px; height: 46px;
    background: var(--orange); border-radius: 7px;
    font-weight: 300; font-size: 40px; line-height: 46px; text-align: center; letter-spacing: -.5px;
  }
  .title-main {
    position: absolute; top: 212px; left: 0; width: 100%;
    text-align: center; font-weight: 800; font-size: 98px; letter-spacing: -2px; line-height: 1.05;
  }
  .version {
    position: absolute; top: 322px; left: 0; width: 100%;
    text-align: center; font-weight: 300; font-size: 23px;
  }
  .plans {
    position: absolute; top: 383px; left: 21px; width: 885px;
    border-collapse: collapse; table-layout: fixed;
    border-radius: 33px 33px 0 27px; overflow: hidden;
  }
  .plans col.feature { width: 465px; }
  .plans col.tier-a { width: 124px; }
  .plans col.tier-b { width: 125px; }
  .plans col.tier-c { width: 171px; }
  .plans th, .plans td { padding: 0; }
  .plans thead th {
    background: var(--orange); height: 54px; font-weight: 600; font-size: 25px; text-align: center;
  }
  .plans thead th.agreement { text-align: left; padding-left: 38px; font-size: 29px; padding-top: 6px; }
  .plans tbody tr { background: var(--row); }
  .plans tbody td { border-bottom: 1px solid var(--line); text-align: center; font-size: 20px; font-weight: 400; }
  .plans tbody td + td { border-left: 1px solid var(--line); }
  .plans tbody td.item { text-align: left; padding-left: 38px; font-weight: 300; font-size: 20px; white-space: nowrap; }
  .plans tr.section td.item { font-weight: 500; font-size: 28px; }
  .plans tr.band td { background: var(--orange); border: none; }
  .plans tr.band td.item { font-weight: 500; font-size: 28px; }
  .tick, .cross { display: inline-block; vertical-align: middle; }
  .tick { width: 30px; height: 24px; }
  .cross { width: 25px; height: 25px; }
  .company {
    position: absolute; top: 1126px; left: 0; width: 100%;
    text-align: center; font-weight: 400; font-size: 17px;
  }
  .contacts {
    position: absolute; top: 1156px; left: 61px; right: 60px;
    display: flex; justify-content: space-between; font-weight: 300; font-size: 15px;
  }
  .contact { display: flex; align-items: center; gap: 8px; }
  .contact svg { flex: none; }
</style>
</head>
<body>
<svg width="0" height="0" style="position:absolute">
  <defs>
    <symbol id="tick-mark" viewBox="0 0 30 24">
      <path d="M3 12 L11 20 L27 4" fill="none" stroke="var(--tick)" stroke-width="5" stroke-linecap="round" stroke-linejoin="round"/>
    </symbol>
    <symbol id="cross-mark" viewBox="0 0 25 25">
      <path d="M3 3 L22 22 M22 3 L3 22" fill="none" stroke="var(--cross)" stroke-width="5.5"/>
    </symbol>
  </defs>
</svg>

<div class="network-backdrop" role="img" aria-label="Glowing blue network of connected nodes across a dark navy background"></div>

<header class="brand">
  <span class="brand-dot"></span>
  <div class="brand-text">
    <span class="brand-name">NODEWISE</span>
    <span class="brand-tagline">THE TEAM FOR ALL YOUR I.T SOLUTIONS</span>
  </div>
</header>

<div class="title-pill">MANAGED SERVICES</div>
<h1 class="title-main">FRAMEWORK</h1>
<p class="version">Version 1.0 | Updated: April 2024</p>

<table class="plans">
  <colgroup><col class="feature"><col class="tier-a"><col class="tier-b"><col class="tier-c"></colgroup>
  <thead>
    <tr><th class="agreement">Managed Services Agreement</th><th>Essential</th><th>Business</th><th>Professional</th></tr>
  </thead>
  <tbody>
    <tr class="section" style="height:44px"><td class="item">Support</td>
      <td><svg class="tick"><use href="#tick-mark"/></svg></td><td><svg class="tick"><use href="#tick-mark"/></svg></td><td><svg class="tick"><use href="#tick-mark"/></svg></td></tr>
    <tr style="height:39px"><td class="item">Unlimited Remote Support 7am to 6pm</td>
      <td><svg class="tick"><use href="#tick-mark"/></svg></td><td><svg class="tick"><use href="#tick-mark"/></svg></td><td><svg class="tick"><use href="#tick-mark"/></svg></td></tr>
    <tr style="height:37px"><td class="item">3rd Party Vendor Support</td>
      <td><svg class="tick"><use href="#tick-mark"/></svg></td><td><svg class="tick"><use href="#tick-mark"/></svg></td><td><svg class="tick"><use href="#tick-mark"/></svg></td></tr>
    <tr style="height:40px"><td class="item">Reactive Onsite Support 8am to 5pm</td>
      <td>VIP Rates</td><td><svg class="tick"><use href="#tick-mark"/></svg></td><td><svg class="tick"><use href="#tick-mark"/></svg></td></tr>
    <tr style="height:36px"><td class="item">After-Hours Support</td>
      <td>VIP Rates</td><td>VIP Rates</td><td><svg class="tick"><use href="#tick-mark"/></svg></td></tr>
    <tr class="band" style="height:44px"><td class="item" colspan="4">Service</td></tr>
    <tr style="height:38px"><td class="item">Guaranteed SLA Response Times</td>
      <td><svg class="tick"><use href="#tick-mark"/></svg></td><td><svg class="tick"><use href="#tick-mark"/></svg></td><td><svg class="tick"><use href="#tick-mark"/></svg></td></tr>
    <tr style="height:44px"><td class="item">24x7 Website &amp; Infrastructure Monitoring</td>
      <td><svg class="tick"><use href="#tick-mark"/></svg></td><td><svg class="tick"><use href="#tick-mark"/></svg></td><td><svg class="tick"><use href="#tick-mark"/></svg></td></tr>
    <tr style="height:41px"><td class="item">Secure Web Content Filtering</td>
      <td><svg class="tick"><use href="#tick-mark"/></svg></td><td><svg class="tick"><use href="#tick-mark"/></svg></td><td><svg class="tick"><use href="#tick-mark"/></svg></td></tr>
    <tr style="height:44px"><td class="item">Backup Monitoring</td>
      <td><svg class="tick"><use href="#tick-mark"/></svg></td><td><svg class="tick"><use href="#tick-mark"/></svg></td><td><svg class="tick"><use href="#tick-mark"/></svg></td></tr>
    <tr style="height:44px"><td class="item">Desktop Operating System Patching &amp; Updating</td>
      <td><svg class="tick"><use href="#tick-mark"/></svg></td><td><svg class="tick"><use href="#tick-mark"/></svg></td><td><svg class="tick"><use href="#tick-mark"/></svg></td></tr>
    <tr style="height:44px"><td class="item">CEO / MD Home Tech Support</td>
      <td><svg class="tick"><use href="#tick-mark"/></svg></td><td><svg class="tick"><use href="#tick-mark"/></svg></td><td><svg class="tick"><use href="#tick-mark"/></svg></td></tr>
    <tr style="height:44px"><td class="item">Monthly Tech Site Visit</td>
      <td><svg class="cross"><use href="#cross-mark"/></svg></td><td>Quarterly</td><td>Monthly</td></tr>
    <tr style="height:45px"><td class="item">Short Term Loan Equipment</td>
      <td><svg class="cross"><use href="#cross-mark"/></svg></td><td>1 Month</td><td>3 Months</td></tr>
    <tr style="height:44px"><td class="item">Adds / Moves / Changes (Staff)</td>
      <td><svg class="tick"><use href="#tick-mark"/></svg></td><td><svg class="tick"><use href="#tick-mark"/></svg></td><td><svg class="tick"><use href="#tick-mark"/></svg></td></tr>
    <tr style="height:44px"><td class="item">Adds / Moves / Changes (Workstations)</td>
      <td>VIP Rates</td><td>VIP Rates</td><td><svg class="tick"><use href="#tick-mark"/></svg></td></tr>
  </tbody>
</table>

<p class="company">NODEWISE COMPUTER SERVICES PTY LTD</p>
<footer class="contacts">
  <span class="contact">
    <svg width="24" height="17" viewBox="0 0 24 17"><rect x="1" y="1" width="22" height="15" fill="none" stroke="var(--orange)" stroke-width="2"/><path d="M1 1 L12 10 L23 1" fill="none" stroke="var(--orange)" stroke-width="2"/></svg>
    service@nodewisecomputers.com.au
  </span>
  <span class="contact">
    <svg width="16" height="24" viewBox="0 0 16 24"><path d="M8 23 C3 15 1 11 1 8 a7 7 0 0 1 14 0 c0 3 -2 7 -7 15z" fill="var(--orange)"/><circle cx="8" cy="8" r="2.8" fill="var(--white)"/></svg>
    12/40 Harbour St, Eastvale, VIC, 3999
  </span>
  <span class="contact">
    <svg width="26" height="22" viewBox="0 0 26 22"><path d="M1 7 C5 1 21 1 25 7 L21 10 L18 6 H8 L5 10z" fill="var(--orange)"/><path d="M7 10 H19 L23 21 H3z" fill="var(--orange)"/><circle cx="13" cy="15" r="3" fill="var(--navy-deep)"/></svg>
    03 9000 1234
  </span>
</footer>
</body>
</html>
```